Food Hall in Seabright Cove, CA by the Pacific Ocean that has 15 vendors and 2 bars

We need a web page design that highlights our food hall in Seabright Cove, CA. The name of the food hall is Bellwick Food Hall. Inside of the food hall there are 15 different vendors and 2 bars. The place has a beautiful patio and it is by Pacific Ocean. Most of the vendors are local to San Clemente area. The highly anticipated location is opening during the summer of 2025. Website should have a dropdown menu for the different vendors that are in the food hall and people should be able to click to their respective business website. The website should also include link to our social media channels and also a link to provide comments and subscribe for the mailing list.
Target Market(s)
Mostly residents in the Seabright Cove, CA and surrounding areas. Couples, families and tourist alike that are looking for an exceptional dining experience that everyone can find something they like.
Industry/Entity Type
Restaurants
Coding
Coded - Design and coding required
Number of Pages Required
5+ page
Font styles to use
Look and feel

```html
<!DOCTYPE html>
<html lang="en">
<head>
<meta charset="utf-8">
<title>Bellwick Food Hall</title>
<link rel="stylesheet" href="https://fonts.googleapis.com/css2?family=Poppins:wght@300;400;500;600;700;800&display=swap">
<style>
:root{
  --navy:#0b4fa6;
  --blue:#0a5bb0;
  --cyan:#1a9ad6;
  --ink:#1b1b1b;
  --text:#3a3a3a;
  --muted:#555;
  --grey-bg:#f2f2f2;
  --sky-bg:#e8f4fa;
  --white:#fff;
  --line:#d9d9d9;
  --star:#f5b400;
  --quote:#cfe6f3;
  --icon:#8a8a8a;
}
*{box-sizing:border-box;margin:0;padding:0}
html,body{width:1200px;height:3586px;overflow:hidden}
body{font-family:"Poppins",sans-serif;color:var(--text);background:var(--white);position:relative}
a{color:inherit;text-decoration:none}
.btn{position:absolute;display:flex;align-items:center;justify-content:center;font-weight:700;font-size:15px;letter-spacing:.3px}
.btn-outline{border:1.5px solid var(--blue);color:var(--blue);background:var(--white)}
.btn-fill{background:var(--cyan);color:var(--white)}
.sec-title{position:absolute;font-size:36px;font-weight:400;color:var(--ink);line-height:1;letter-spacing:.3px}
.sec-title b{color:var(--cyan);font-weight:700}
.chev{position:absolute;width:18px;height:26px;stroke:#555;stroke-width:2.2;fill:none}
.chev.blue{stroke:var(--blue)}

/* header */
.site-header{position:absolute;left:0;top:0;width:1200px;height:82px;background:var(--white)}
.brand{position:absolute;left:74px;top:30px;font-size:23px;font-weight:700;color:var(--navy);letter-spacing:.3px;line-height:1}
.nav{position:absolute;top:37px;left:526px;display:flex;gap:37px;font-size:12.5px;color:#333;line-height:1;list-style:none}
.nav .current{color:var(--blue);font-weight:600;border-bottom:2px solid var(--blue);padding-bottom:4px}

/* hero */
.hero{position:absolute;left:0;top:82px;width:1200px;height:569px;overflow:hidden}
.hero-photo{position:absolute;inset:0;background:linear-gradient(170deg,#5f86b8 0%,#3b6a99 30%,#2d5b86 55%,#4f6f58 72%,#a89474 100%)}
.hero-photo::after{content:"";position:absolute;inset:0;background:linear-gradient(90deg,rgba(58,80,50,.55) 0%,rgba(0,0,0,0) 45%)}
.hero h1{position:absolute;left:0;width:1200px;top:172px;text-align:center;font-size:57px;font-weight:800;color:var(--white);line-height:1;letter-spacing:.5px}
.hero p{position:absolute;left:0;width:1200px;top:236px;text-align:center;font-size:24px;font-weight:600;color:var(--white);line-height:37px;white-space:nowrap}
.hero .btn{left:511px;top:333px;width:177px;height:56px}
.dots{position:absolute;left:1128px;top:454px;display:flex;flex-direction:column;gap:16px}
.dots span{width:10px;height:10px;border-radius:50%;background:var(--white)}
.dots span.on{background:var(--cyan)}

/* welcome */
.frame-band{position:absolute;background:var(--navy)}
.welcome-photo{position:absolute;left:136px;top:721px;width:451px;height:373px;background:linear-gradient(160deg,#c96a4b 0%,#a8533c 45%,#4c5a4a 80%,#7b7a6a 100%)}
.welcome-kicker{position:absolute;left:617px;top:718px;font-size:36px;font-weight:400;color:var(--ink);line-height:1}
.welcome-title{position:absolute;left:617px;top:758px;font-size:36px;font-weight:700;color:var(--cyan);line-height:1}
.welcome-copy{position:absolute;left:617px;top:801px;font-size:15px;line-height:28px;color:var(--text);white-space:nowrap}
.welcome-copy .tight{line-height:25px;margin-top:1px}

/* vendors */
.vendors{position:absolute;left:0;top:1176px;width:1200px;height:567px;background:var(--grey-bg)}
.vendor{position:absolute;top:127px;width:242px;height:273px;text-align:center}
.vendor.is-active{background:var(--white)}
.vendor-logo{height:164px;background:var(--white);display:flex;align-items:center;justify-content:center;font-size:19px;font-weight:600;color:#222}
.vendor h3{margin-top:22px;font-size:17px;font-weight:700;color:var(--blue);line-height:1}
.vendor p{margin-top:9px;font-size:13.5px;line-height:25px;color:var(--muted)}

/* news */
.news{position:absolute;left:0;top:1743px;width:1200px;height:429px;overflow:hidden}
.news-kicker{position:absolute;left:74px;top:130px;font-size:36px;font-weight:400;color:var(--ink);line-height:1}
.news-title{position:absolute;left:74px;top:172px;font-size:36px;font-weight:700;color:var(--cyan);line-height:1}
.news-card{position:absolute;top:75px;width:245px;height:278px;overflow:hidden}
.news-card .photo{position:absolute;inset:0}
.news-card .shade{position:absolute;left:0;right:0;bottom:0;height:120px;background:linear-gradient(180deg,rgba(0,0,0,0),rgba(0,0,0,.75))}
.news-card .meta{position:absolute;left:15px;bottom:14px;color:var(--white);font-weight:700;font-size:14.5px;line-height:22px;white-space:nowrap}

/* testimonials */
.testi-band{position:absolute;left:0;top:2172px;width:587px;height:299px;background:var(--sky-bg)}
.testi{position:absolute;top:2286px;width:330px;height:278px;background:var(--white);box-shadow:0 2px 10px rgba(0,0,0,.12);text-align:center}
.testi p{position:absolute;left:0;right:0;top:19px;font-size:15px;line-height:27.3px;color:#222;white-space:nowrap}
.testi h4{position:absolute;left:0;right:0;top:202px;font-size:14px;font-weight:700;color:var(--blue)}
.testi .stars{position:absolute;left:122px;top:228px;display:flex;gap:9px}
.stars svg{width:14px;height:14px;fill:var(--star)}
.q{position:absolute;font-family:Georgia,serif;font-size:84px;line-height:1;color:var(--quote);font-weight:700}
.q-open{left:14px;top:4px}
.q-close{right:14px;top:212px}

/* gallery */
.gallery{position:absolute;left:0;top:2645px;width:1200px;height:434px;background:var(--sky-bg)}
.shot{position:absolute;top:164px;width:242px;height:174px}

/* footer */
.foot-col{position:absolute;top:3147px}
.foot-col h5{font-size:15.5px;font-weight:700;color:var(--blue);line-height:1;margin-bottom:14px}
.foot-col ul{list-style:none;font-size:13.5px;line-height:29.6px;color:#333}
.foot-brand h5{font-size:20px;margin-bottom:13px}
.foot-brand p{font-size:13.5px;line-height:24.5px;color:#333;white-space:nowrap}
.contact p{font-size:13.5px;line-height:24px;color:#333}
.rule{position:absolute;left:74px;width:1054px;height:1px;background:var(--line)}
.news-label{position:absolute;left:180px;top:3437px;font-size:19px;font-weight:700;color:var(--blue);line-height:1}
.email-input{position:absolute;left:448px;top:3424px;width:422px;height:48px;border:1px solid #cfcfcf;font-family:inherit;font-size:13.5px;padding-left:15px;color:#333;background:var(--white)}
.subscribe{left:885px;top:3424px;width:139px;height:48px}
.copyright{position:absolute;left:74px;top:3535px;font-size:12.5px;color:#333}
.social{position:absolute;left:956px;top:3532px;display:flex;gap:23px}
.social span{width:18px;height:18px;border-radius:50%;background:var(--icon)}
.social span.on{background:var(--blue)}
</style>
</head>
<body>
<svg width="0" height="0" style="position:absolute">
  <defs>
    <symbol id="left" viewBox="0 0 18 26"><polyline points="14,2 4,13 14,24"/></symbol>
    <symbol id="right" viewBox="0 0 18 26"><polyline points="4,2 14,13 4,24"/></symbol>
    <symbol id="star" viewBox="0 0 20 20"><polygon points="10,1 12.6,7 19,7.5 14,11.8 15.6,18.5 10,15 4.4,18.5 6,11.8 1,7.5 7.4,7"/></symbol>
  </defs>
</svg>

<header class="site-header">
  <div class="brand">BELLWICK FOOD HALL</div>
  <ul class="nav">
    <li class="current">HOME</li>
    <li>ABOUT US</li>
    <li>VENDORS</li>
    <li>NEWS &amp; UPDATES</li>
    <li>REVIEWS</li>
    <li>CONTACT US</li>
  </ul>
</header>

<section class="hero">
  <div class="hero-photo" role="img" aria-label="Coastal cliffs with palm trees above a sandy beach and the ocean"></div>
  <h1>BELLWICK FOOD HALL</h1>
  <p>We are&nbsp; a Food Hall in Seabright Cove, CA by the Pacific<br>Ocean that has 15 vendors and 2 bars.</p>
  <a class="btn btn-fill">READ MORE</a>
  <div class="dots"><span class="on"></span><span></span><span></span><span></span></div>
</section>

<section>
  <div class="frame-band" style="left:0;top:711px;width:136px;height:393px"></div>
  <div class="frame-band" style="left:0;top:711px;width:557px;height:10px"></div>
  <div class="frame-band" style="left:0;top:1094px;width:306px;height:10px"></div>
  <div class="welcome-photo" role="img" aria-label="Red brick food hall building with large windows and planters at the entrance"></div>
  <div class="welcome-kicker">WELCOME TO</div>
  <div class="welcome-title">BELLWICK FOOD HALL</div>
  <div class="welcome-copy">
    <p>Sed ut perspiciatis unde omnis iste natus error sit voluptatem<br>accusantium doloremque laudantium, totam rem aperiam, eaque<br>ipsa quae ab illo inventore veritatis et quasi architecto beatae<br>vitae dicta sunt explicabo. Nemo enim ipsam voluptatem quia<br>voluptas sit aspernatur aut odit aut fugit, sed quia consequuntur<br>magni dolores eos qui ratione voluptatem sequi nesciunt.</p>
    <p class="tight">Duis aute irure dolor in reprehenderit in voluptate velit esse cillum<br>dolore eu fugiat nulla pariatur.</p>
  </div>
  <a class="btn btn-outline" style="left:615px;top:1038px;width:178px;height:56px">READ MORE</a>
</section>

<section class="vendors">
  <h2 class="sec-title" style="left:0;width:1200px;text-align:center;top:58px">OUR <b>FOOD VENDORS</b></h2>
  <svg class="chev" style="left:44px;top:245px"><use href="#left"/></svg>
  <svg class="chev" style="left:1137px;top:245px"><use href="#right"/></svg>
  <div class="vendor" style="left:74px">
    <div class="vendor-logo">Dolce Forno</div>
    <h3>DOLCE FORNO</h3>
    <p>Duis aute irure dolor in reprehen<br>derit in voluptate velit.</p>
  </div>
  <div class="vendor is-active" style="left:345px">
    <div class="vendor-logo">Ember Hot Chicken</div>
    <h3>EMBER HOT CHICKEN</h3>
    <p>Duis aute irure dolor in reprehen<br>derit in voluptate velit.</p>
  </div>
  <div class="vendor" style="left:614px">
    <div class="vendor-logo">Orbit Burgers</div>
    <h3>ORBIT BURGERS</h3>
    <p>Duis aute irure dolor in reprehen<br>derit in voluptate velit.</p>
  </div>
  <div class="vendor" style="left:885px">
    <div class="vendor-logo">Tidewater Catering</div>
    <h3>DOLCE FORNO</h3>
    <p>Duis aute irure dolor in reprehen<br>derit in voluptate velit.</p>
  </div>
  <a class="btn btn-outline" style="left:511px;top:448px;width:178px;height:56px">SEE ALL VENDORS</a>
</section>

<section class="news">
  <div class="news-kicker">LATEST NEWS</div>
  <div class="news-title">&amp; UPDATES</div>
  <a class="btn btn-outline" style="left:74px;top:238px;width:179px;height:56px">VEWLL NEWS</a>
  <svg class="chev blue" style="left:73px;top:325px"><use href="#left"/></svg>
  <svg class="chev" style="left:112px;top:325px"><use href="#right"/></svg>
  <article class="news-card" style="left:342px">
    <div class="photo" role="img" aria-label="Smiling vendor in a red apron standing in a market aisle" style="background:linear-gradient(170deg,#c8a27a,#b83a35 60%,#6d4a3a)"></div>
    <div class="shade"></div>
    <div class="meta">APR, 23, 2025<br>NEMO ENIM IPSAM VOLUPT<br>ATEM QUIA</div>
  </article>
  <article class="news-card" style="left:617px">
    <div class="photo" role="img" aria-label="Two people sharing a box of fresh produce indoors" style="background:linear-gradient(170deg,#5c6b70,#3d3a36 55%,#7a5a44)"></div>
    <div class="shade"></div>
    <div class="meta">APR, 23, 2025<br>NEMO ENIM IPSAM VOLUPT<br>ATEM QUIA</div>
  </article>
  <article class="news-card" style="left:885px">
    <div class="photo" role="img" aria-label="Shop owner holding a packaged product in front of stocked shelves" style="background:linear-gradient(170deg,#a58a66,#6d5a45 55%,#3b3b33)"></div>
    <div class="shade"></div>
    <div class="meta">APR, 23, 2025<br>NEMO ENIM IPSAM VOLUPT<br>ATEM QUIA</div>
  </article>
  <article class="news-card" style="left:1154px">
    <div class="photo" role="img" aria-label="Customer at a food stall counter" style="background:linear-gradient(170deg,#d6b58a,#8a6a4c 60%,#4a3c32)"></div>
    <div class="shade"></div>
    <div class="meta">APR, 23, 2025<br>NEMO ENIM IPSAM VOLUPT<br>ATEM QUIA</div>
  </article>
</section>

<section>
  <div class="testi-band"></div>
  <svg class="chev blue" style="left:73px;top:2214px"><use href="#left"/></svg>
  <svg class="chev" style="left:112px;top:2214px"><use href="#right"/></svg>
  <h2 class="sec-title" style="right:70px;top:2212px">CLIENT <b>TESTIMONIALS</b></h2>

  <div class="testi" style="left:74px">
    <span class="q q-open">&ldquo;</span><span class="q q-close">&rdquo;</span>
    <p>Nemo enim ipsam voluptatem<br>quia voluptas sit aspernatur aut odit<br>aut fugit, sed quia consequuntur<br>magni dolores&nbsp; enim ipsam<br>voluptatem quia voluptas sit<br>aspernatur aut odit aut..</p>
    <h4>NAME HEADING</h4>
    <div class="stars"><svg><use href="#star"/></svg><svg><use href="#star"/></svg><svg><use href="#star"/></svg><svg><use href="#star"/></svg></div>
  </div>
  <div class="testi" style="left:436px">
    <span class="q q-open">&ldquo;</span><span class="q q-close">&rdquo;</span>
    <p>Nemo enim ipsam voluptatem<br>quia voluptas sit aspernatur aut odit<br>aut fugit, sed quia consequuntur<br>magni dolores&nbsp; enim ipsam<br>voluptatem quia voluptas sit<br>aspernatur aut odit aut..</p>
    <h4>NAME HEADING</h4>
    <div class="stars"><svg><use href="#star"/></svg><svg><use href="#star"/></svg><svg><use href="#star"/></svg><svg><use href="#star"/></svg></div>
  </div>
  <div class="testi" style="left:798px">
    <span class="q q-open">&ldquo;</span><span class="q q-close">&rdquo;</span>
    <p>Nemo enim ipsam voluptatem<br>quia voluptas sit aspernatur aut odit<br>aut fugit, sed quia consequuntur<br>magni dolores&nbsp; enim ipsam<br>voluptatem quia voluptas sit<br>aspernatur aut odit aut..</p>
    <h4>NAME HEADING</h4>
    <div class="stars"><svg><use href="#star"/></svg><svg><use href="#star"/></svg><svg><use href="#star"/></svg><svg><use href="#star"/></svg></div>
  </div>
</section>

<section class="gallery">
  <h2 class="sec-title" style="left:0;width:1200px;text-align:center;top:93px">PHOTO <b>GALLERY</b></h2>
  <svg class="chev" style="left:44px;top:239px"><use href="#left"/></svg>
  <svg class="chev" style="left:1137px;top:239px"><use href="#right"/></svg>
  <div class="shot" style="left:74px;background:linear-gradient(160deg,#c9c3b6,#b59a78 55%,#6a5a4c)" role="img" aria-label="Two friends sharing food at a counter"></div>
  <div class="shot" style="left:345px;background:linear-gradient(180deg,#d9742e,#8a4a2a 45%,#b7aca0)" role="img" aria-label="Bright food hall interior with orange ceiling and seating"></div>
  <div class="shot" style="left:614px;background:linear-gradient(160deg,#c9d0d4,#3a3a3a 55%,#8a7a6a)" role="img" aria-label="Modern bar counter with stocked shelves and large windows"></div>
  <div class="shot" style="left:885px;background:linear-gradient(170deg,#6a4a32,#b47a44 55%,#3c2c22)" role="img" aria-label="Fresh bread loaves on a bakery counter"></div>
</section>

<footer>
  <div class="foot-col foot-brand" style="left:74px;top:3143px">
    <h5>BELLWICK FOOD HALL</h5>
    <p>Duis aute irure dolor in repre<br>henderit in voluptate velit esse<br>cillum dolore eu fugiat nulla pa<br>riatur commodo.</p>
  </div>
  <div class="foot-col" style="left:383px">
    <h5>QUICK LINKS</h5>
    <ul><li>Home</li><li>About Us</li><li>Vendors</li><li>News &amp; updates</li><li>Reviews</li><li>Contact Us</li></ul>
  </div>
  <div class="foot-col" style="left:632px">
    <h5>RESOURCES</h5>
    <ul><li>Excepteur sint</li><li>Occaecat cupidatat</li><li>Proident</li><li>Sunt in culpa</li><li>Excepteur sint</li></ul>
  </div>
  <div class="foot-col contact" style="left:898px">
    <h5>CONTACT INFO</h5>
    <p style="margin-top:-2px">480 Tidewater Lane,<br>Seabright Cove, California 95555</p>
    <p style="margin-top:8px">+1 555-010-2468</p>
    <p style="margin-top:8px">hello@bellwickhall.com</p>
  </div>

  <div class="rule" style="top:3395px"></div>
  <div class="news-label">NEWSLETTER SUBSCRIBE</div>
  <input class="email-input" type="email" placeholder="Enter Email Address" aria-label="Email address">
  <a class="btn btn-fill subscribe">SUBSCRIBE</a>
  <div class="rule" style="top:3498px"></div>

  <div class="copyright">Copyright &copy; 2025 Bellwick Food Hall All Right Reserved. Privacy Policy</div>
  <div class="social" aria-label="Social media links">
    <span aria-label="Social link 1"></span>
    <span class="on" aria-label="Social link 2"></span>
    <span aria-label="Social link 3"></span>
    <span aria-label="Social link 4"></span>
    <span aria-label="Social link 5"></span>
  </div>
</footer>
</body>
</html>
```